New Business Card Design Project

Looking for a modern business card design for an import distribution business for industrial technical products. The winning design will translate modern, sophistication, technical, professional and sustainable.

Target Market(s)

Technical customers

Industry/Entity Type

Business

Contact Information for Business Card

Dean Harlow
Sales Manager
M: 0471 625 183
P: 1300 872 619
dean@volkarsystems.com.au
4/18 Galloway Crest Road
Kellmont Park NSW 2163
www.volkarsystems.com.au

Font styles to use
Sans Serif

Colors
ec1f27
606060
000000
fbfbfb

Requirements
Must have
• My Logo which is the Volkar Systems logo attached
Nice to have
• Eurostile Bold font

```html
<!DOCTYPE html>
<html lang="en">
<head>
<meta charset="utf-8">
<title>Volkar Systems – Business Cards</title>
<link rel="stylesheet" href="https://fonts.googleapis.com/css2?family=Source+Sans+3:wght@400;600&display=swap">
<style>
  :root {
    --backdrop: #000000;
    --card: #333437;
    --card-light: #38393c;
    --red: #e0332c;
    --grey: #606060;
    --text: #fbfbfb;
    --rule: #3f4043;
  }
  html, body {
    margin: 0;
    padding: 0;
    width: 1200px;
    height: 900px;
    overflow: hidden;
    background: var(--backdrop);
    font-family: "Source Sans 3", "Myriad Pro", Arial, sans-serif;
  }
  .canvas {
    position: relative;
    width: 1200px;
    height: 900px;
  }
  .card {
    position: absolute;
    top: 271px;
    width: 457px;
    height: 281px;
    border-radius: 14px;
    background: radial-gradient(ellipse at 50% 40%, var(--card-light), var(--card) 75%);
    overflow: hidden;
  }
  .card--front { left: 137px; }
  .card--back { left: 626px; }

  .brand-square {
    position: absolute;
    left: 49px;
    top: 94px;
    width: 101px;
    height: 101px;
    background: var(--red);
  }
  .divider {
    position: absolute;
    left: 196px;
    top: 48px;
    width: 1px;
    height: 228px;
    background: var(--rule);
  }
  .details {
    position: absolute;
    left: 218px;
    top: 58px;
    color: var(--text);
    font-size: 13px;
    line-height: 17px;
  }
  .details__name {
    margin: 0;
    color: var(--red);
    font-size: 18px;
    font-weight: 600;
    line-height: 22px;
  }
  .details__role { margin: 0 0 12px; }
  .details__address { margin: 0 0 14px; font-style: normal; }
  .contact-list { list-style: none; margin: 0; padding: 0; }
  .contact-list li {
    display: flex;
    align-items: center;
    height: 19px;
  }
  .contact-list svg {
    width: 10px;
    height: 10px;
    margin: 0 7px 0 0;
    fill: var(--red);
    flex: none;
  }

  .lockup {
    position: absolute;
    left: 88px;
    top: 117px;
    display: flex;
    align-items: center;
    gap: 14px;
  }
  .lockup__square {
    width: 48px;
    height: 48px;
    background: var(--red);
  }
  .lockup__name {
    color: var(--red);
    font-size: 30px;
    font-weight: 600;
    letter-spacing: 1px;
    text-transform: uppercase;
    white-space: nowrap;
  }
</style>
</head>
<body>
<main class="canvas">
  <section class="card card--front" aria-label="Business card front">
    <div class="brand-square" aria-hidden="true"></div>
    <div class="divider" aria-hidden="true"></div>
    <div class="details">
      <h1 class="details__name">Dean Harlow</h1>
      <p class="details__role">Sales Manager</p>
      <address class="details__address">4/18 Galloway Crest Road<br>Kellmont Park NSW 2163</address>
      <ul class="contact-list">
        <li><svg viewBox="0 0 10 10" aria-hidden="true"><path d="M3 0h4a1 1 0 0 1 1 1v8a1 1 0 0 1-1 1H3a1 1 0 0 1-1-1V1a1 1 0 0 1 1-1zm0 1.5v6h4v-6z"/></svg>0471 625 183</li>
        <li><svg viewBox="0 0 10 10" aria-hidden="true"><path d="M2 0.5l2 2-1 1.2c.6 1.3 1.6 2.3 2.9 2.9l1.2-1 2 2-1.3 1.6C4 9 1 6 0.5 1.7z"/></svg>1300 872 619</li>
        <li><svg viewBox="0 0 10 10" aria-hidden="true"><path d="M0 2h10v6H0zm.8.8L5 5.6l4.2-2.8z" fill-rule="evenodd"/></svg>dean@volkarsystems.com.au</li>
        <li><svg viewBox="0 0 10 10" aria-hidden="true"><circle cx="5" cy="5" r="4.6"/></svg>www.volkarsystems.com.au</li>
      </ul>
    </div>
  </section>

  <section class="card card--back" aria-label="Business card back">
    <div class="lockup">
      <div class="lockup__square" aria-hidden="true"></div>
      <span class="lockup__name">Volkar Systems</span>
    </div>
  </section>
</main>
</body>
</html>
```